Ridge 9 Ridge Turbine Rentals Pty Ltd

We are a hire company based on the Gold Coast in Australia, we Hire out Generators to construction sites, music festivals, parties, fetes etc. Anywhere where power is required we can provide it.

Ridge 9 Ridge Turbine Rentals pty Ltd also provides all leads, distribution boards, Qualified Electricians to perform all connections. we offer refuelling services and mechanical services. 24Hr on call service - to an actual english speaking operator.

Slogan ''Power Anywhere Anytime"

Industry/Entity Type

Construction

Contact Information for Business Card

M: 0417285963
E: bookings@ridge9ridgeturbinerentals.com.au

```html
<!DOCTYPE html>
<html lang="en">
<head>
<meta charset="utf-8">
<title>Ridge 9 Ridge Turbine Rentals – Business Card</title>
<link href="https://fonts.googleapis.com/css2?family=Open+Sans:wght@300;400;700&display=swap" rel="stylesheet">
<style>
  :root {
    --page: #d9dadc;
    --card-front: #050505;
    --card-back: #1a5e85;
    --ink-white: #ffffff;
    --ink-dark: #0b1b26;
    --rule: #050b10;
    --accent: #6fb6d6;
  }
  * { box-sizing: border-box; margin: 0; padding: 0; }
  html, body { width: 1200px; height: 900px; overflow: hidden; }
  body {
    background: var(--page);
    font-family: "Open Sans", Arial, sans-serif;
    display: flex;
    flex-direction: column;
    align-items: center;
    justify-content: center;
    gap: 56px;
  }
  .card {
    position: relative;
    width: 640px;
    height: 366px;
    border-radius: 22px;
    overflow: hidden;
  }
  .card--front { background: var(--card-front); }
  .card--back { background: var(--card-back); }

  .brand {
    position: absolute;
    display: flex;
    align-items: center;
    gap: 14px;
  }
  .brand__mark {
    width: 40px;
    height: 40px;
    background: var(--accent);
    flex: none;
  }
  .brand__name {
    color: var(--ink-white);
    font-weight: 700;
    font-size: 21px;
    line-height: 1;
    white-space: nowrap;
  }

  .card--front .brand { left: 40px; top: 218px; }
  .slogan {
    position: absolute;
    left: 40px;
    bottom: 30px;
    color: var(--ink-white);
    font-weight: 300;
    font-size: 17px;
    letter-spacing: 0.6px;
  }

  .card--back .brand { left: 40px; top: 130px; }
  .divider {
    position: absolute;
    top: 268px;
    height: 2px;
    background: var(--rule);
  }
  .divider--left { left: 0; width: 30px; }
  .divider--right { left: 262px; right: 0; }
  .person {
    position: absolute;
    left: 40px;
    top: 250px;
  }
  .person__name {
    color: var(--ink-white);
    font-weight: 700;
    font-size: 29px;
    line-height: 1.1;
    letter-spacing: 0.3px;
  }
  .person__role {
    color: var(--ink-dark);
    font-size: 14px;
    letter-spacing: 0.6px;
    line-height: 1;
  }
  .contact {
    position: absolute;
    right: 24px;
    top: 284px;
    list-style: none;
    text-align: right;
    color: var(--ink-white);
    font-size: 15px;
    line-height: 1.6;
  }
  .contact__item { display: flex; align-items: center; justify-content: flex-end; gap: 8px; }
  .contact__icon { width: 13px; height: 13px; flex: none; }
</style>
</head>
<body>
  <section class="card card--front" aria-label="Card front">
    <div class="brand">
      <span class="brand__mark" aria-hidden="true"></span>
      <span class="brand__name">Ridge 9 Ridge Turbine Rentals</span>
    </div>
    <p class="slogan">POWER ANYWHERE ANYTIME</p>
  </section>

  <section class="card card--back" aria-label="Card back">
    <div class="brand">
      <span class="brand__mark" aria-hidden="true"></span>
      <span class="brand__name">Ridge 9 Ridge Turbine Rentals</span>
    </div>

    <span class="divider divider--left"></span>
    <span class="divider divider--right"></span>

    <div class="person">
      <p class="person__name">LIAM CARTER</p>
      <p class="person__role">DIRECTOR</p>
    </div>

    <ul class="contact">
      <li class="contact__item">
        <span>0417285963</span>
        <svg class="contact__icon" viewBox="0 0 12 12" aria-hidden="true">
          <rect x="3" y="0.8" width="6" height="10.4" rx="1" fill="none" stroke="#fff" stroke-width="1.2"/>
          <line x1="5.2" y1="9.3" x2="6.8" y2="9.3" stroke="#fff" stroke-width="1"/>
        </svg>
      </li>
      <li class="contact__item">
        <span>bookings@ridge9ridgeturbinerentals.com.au</span>
        <svg class="contact__icon" viewBox="0 0 12 12" aria-hidden="true">
          <rect x="0.8" y="2.5" width="10.4" height="7.5" fill="none" stroke="#fff" stroke-width="1.2"/>
          <polyline points="0.8,2.5 6,6.8 11.2,2.5" fill="none" stroke="#fff" stroke-width="1.2"/>
        </svg>
      </li>
    </ul>
  </section>
</body>
</html>
```